BoltCrest Screw Box and Carton Design

We are BoltCrest, a new screw and nail supplier from Ireland. We need box designs branded for our new launch of screws and nails, Outer carton and inner individual boxes. We would like our branding to portray the image of a professional company. We have our logo attached which we would like to stand out so that people recognise the box if it were to be seen from a distance or in a shop.

Target Market(s)

Construction Industry

Industry/Entity Type

Construction

Contact Information for Business Card

Declan Murtagh
Owner
07482619037
declan@boltcrest.co.uk

Font styles to use
Sans Serif

Colors
3277b5

Requirements
Must have
• The Carton should be cost effective for the box maker. The carton will contain 10 boxes. If you could design them in such a way that they can be manipulated easily to cater for the various sizes. The internal boxes that hold the screws will have colour. I like the layout of the Korvex box where the lid folds out over the front of the box. Blue colour #009ee2 Grey colour #4a4a49
Nice to have
• I would like some upgraded design to the original BoltCrest box in the picture. I feel that this design does not cater well for labels or information to be placed on the box.

```html
<!DOCTYPE html>
<html lang="en">
<head>
<meta charset="utf-8">
<title>BoltCrest Screw Box – Flat Artwork</title>
<link href="https://fonts.googleapis.com/css2?family=Titillium+Web:wght@700&family=Open+Sans:wght@600&display=swap" rel="stylesheet">
<style>
  :root {
    --brand-blue: #009ee2;
    --brand-blue-deep: #0a7fb8;
    --brand-grey: #4a4a49;
    --brand-grey-dark: #3a3a3a;
    --ink-white: #ffffff;
    --ink-silver: #d9d9d9;
    --page: #ffffff;
    --fold: rgba(255,255,255,0.35);
  }
  html, body {
    margin: 0;
    padding: 0;
    width: 1200px;
    height: 1200px;
    overflow: hidden;
    background: var(--page);
  }
  .box-net {
    display: block;
    width: 1200px;
    height: 1200px;
  }
  .panel-blue { fill: var(--brand-blue); }
  .panel-grey { fill: var(--brand-grey); }
  .panel-grey-dark { fill: var(--brand-grey-dark); }
  .fold-line { stroke: var(--fold); stroke-width: 2; stroke-dasharray: 6 6; fill: none; }
  .wordmark {
    font-family: "Titillium Web", sans-serif;
    font-weight: 700;
    letter-spacing: 1px;
  }
  .wordmark--white { fill: var(--ink-white); }
  .wordmark--silver { fill: var(--ink-silver); }
  .tagline {
    font-family: "Open Sans", sans-serif;
    font-weight: 600;
    fill: var(--ink-white);
    letter-spacing: 1px;
  }
</style>
</head>
<body>
<svg class="box-net" viewBox="0 0 1200 1200" xmlns="http://www.w3.org/2000/svg" aria-label="BoltCrest screw box artwork, flat layout">
  <defs>
    <linearGradient id="lidShade" x1="0" y1="0" x2="0" y2="1">
      <stop offset="0" stop-color="#009ee2"/>
      <stop offset="1" stop-color="#0a7fb8"/>
    </linearGradient>
    <clipPath id="clipBody"><rect x="390" y="380" width="420" height="520"/></clipPath>
    <clipPath id="clipSide"><rect x="390" y="640" width="420" height="260"/></clipPath>
    <clipPath id="clipLid"><path d="M390 140 H565 A35 35 0 0 0 635 140 H810 V380 H390 Z"/></clipPath>
  </defs>

  <!-- Lid flap (folds over the front) -->
  <g class="lid-flap" clip-path="url(#clipLid)">
    <rect x="390" y="140" width="420" height="240" fill="url(#lidShade)"/>
    <polygon class="panel-grey" points="600,140 810,140 810,290"/>
    <text class="wordmark wordmark--white" x="600" y="292" font-size="64" text-anchor="middle">BOLTCREST</text>
    <text class="tagline" x="600" y="330" font-size="22" text-anchor="middle">SCREWS AND NAILS</text>
  </g>

  <!-- Top and long side panels -->
  <g class="body-panels" clip-path="url(#clipBody)">
    <rect class="panel-blue" x="390" y="380" width="420" height="260"/>
    <g class="side-panel" clip-path="url(#clipSide)">
      <rect class="panel-blue" x="390" y="640" width="420" height="260"/>
      <polygon class="panel-grey" points="390,900 810,760 810,900"/>
      <text class="wordmark wordmark--white" x="420" y="730" font-size="50" transform="rotate(12 420 730)">BOLTCREST</text>
    </g>
    <text class="wordmark wordmark--white" x="600" y="420" font-size="26" text-anchor="middle" transform="rotate(180 600 411)">BOLTCREST</text>
    <text class="wordmark wordmark--white" x="560" y="610" font-size="26" text-anchor="middle">BOLTCREST</text>
    <text class="wordmark wordmark--white" x="728" y="640" font-size="96" text-anchor="middle" textLength="480" lengthAdjust="spacingAndGlyphs" transform="rotate(90 728 640)">BOLTCREST</text>
  </g>

  <!-- Left end panel -->
  <g class="end-panel end-panel--left">
    <rect class="panel-grey-dark" x="150" y="640" width="240" height="260"/>
    <text class="wordmark wordmark--silver" x="270" y="782" font-size="34" text-anchor="middle">BOLTCREST</text>
  </g>

  <!-- Right end panel -->
  <g class="end-panel end-panel--right">
    <rect class="panel-grey-dark" x="810" y="640" width="240" height="260"/>
    <text class="wordmark wordmark--silver" x="930" y="782" font-size="34" text-anchor="middle">BOLTCREST</text>
  </g>

  <!-- Fold lines -->
  <g class="folds">
    <line class="fold-line" x1="390" y1="380" x2="810" y2="380"/>
    <line class="fold-line" x1="390" y1="640" x2="810" y2="640"/>
    <line class="fold-line" x1="390" y1="640" x2="390" y2="900"/>
    <line class="fold-line" x1="810" y1="640" x2="810" y2="900"/>
  </g>
</svg>
</body>
</html>
```